Local Motorsports Photography Business Card Design

Looking for a Logo and Business Card design for my father who is a local photographer based in Perth operating under the business name "KLV Photography". Specializing in Motorsports (Torque Racers/Gridcycles/Vorlen Rally) and events photography.
Would like it to look professional, while still maintaining a local/personal feel. Color\Design of the Logo and Card are open to your own interpretation, but should limit the color scheme to around 2-3 colors.
Design should be a logo one side and contact details on the rear. The website currently is very simple and a generic template and should not be used as a basis for design.
Industry/Entity Type
Business
Contact Information for Business Card
Name: Gareth Pindle
Website: www.klvphotography-example.com.au
Email: gareth@klvphotography-example.com.au
Phone: 0455 917 263
Look and feel
Each slider illustrates characteristics of the customer's brand and the style your logo design should communicate.

```html
<!DOCTYPE html>
<html lang="en">
<head>
<meta charset="utf-8">
<title>KLV Photography – Business Card</title>
<link rel="stylesheet" href="https://fonts.googleapis.com/css2?family=Exo+2:wght@400;600;700&display=swap">
<style>
  :root {
    --canvas: #ecebe8;
    --ink: #1e1f21;
    --frame-dark: #26272a;
    --sky: #3eaee6;
    --sky-light: #bfe4f7;
    --sky-pale: #e6f5fc;
    --paper: #ffffff;
    --paper-shade: #eeeeee;
    --muted: #4a4d52;
  }
  * { box-sizing: border-box; margin: 0; padding: 0; }
  html, body { width: 1057px; height: 1200px; overflow: hidden; }
  body {
    background: var(--canvas);
    font-family: "Exo 2", "Segoe UI", sans-serif;
    color: var(--ink);
    position: relative;
  }
  .card {
    position: absolute;
    top: 215px;
    width: 440px;
    height: 770px;
    box-shadow: 0 10px 30px rgba(0,0,0,.18);
  }
  .card--contact { left: 70px; background: var(--frame-dark); padding: 16px; }
  .card--brand { left: 547px; background: var(--sky); padding: 22px; }

  .card__inner {
    position: relative;
    width: 100%;
    height: 100%;
    background: linear-gradient(180deg, var(--paper) 0%, var(--paper-shade) 100%);
    overflow: hidden;
  }

  /* brand lockup */
  .brand {
    display: flex;
    align-items: center;
    gap: 14px;
    font-weight: 700;
    color: var(--ink);
    letter-spacing: .5px;
  }
  .brand__dot {
    width: 46px; height: 46px;
    border-radius: 50%;
    background: var(--sky);
    flex: none;
  }
  .brand__name { font-size: 34px; line-height: 1; }

  .card--contact .brand { position: absolute; top: 72px; left: 38px; }

  .person { position: absolute; top: 170px; left: 38px; }
  .person__name {
    font-size: 30px; font-weight: 600; letter-spacing: 2px;
    text-transform: uppercase;
  }
  .person__role {
    margin-top: 4px;
    font-size: 14px; font-weight: 400; letter-spacing: 2px;
    text-transform: uppercase; color: var(--muted);
  }

  .contact-band {
    position: absolute;
    left: 0; right: 0; top: 250px; bottom: 60px;
    background: linear-gradient(180deg, var(--sky-pale) 0%, var(--sky-light) 45%, var(--sky) 100%);
    clip-path: polygon(0 0, 100% 26%, 100% 100%, 0 100%);
  }
  .contact-list {
    position: absolute;
    top: 300px; left: 38px;
    list-style: none;
  }
  .contact-list li {
    display: flex; align-items: center; gap: 14px;
    height: 44px;
    font-size: 16px; color: var(--ink);
  }
  .icon {
    width: 26px; height: 26px;
    background: var(--frame-dark);
    display: flex; align-items: center; justify-content: center;
    flex: none;
  }
  .icon svg { width: 16px; height: 16px; }

  .address-bar {
    position: absolute; left: 0; right: 0; bottom: 0;
    height: 60px;
    background: var(--frame-dark);
    display: flex; align-items: center; gap: 14px;
    padding-left: 38px;
    color: var(--paper);
    font-size: 15px;
  }
  .address-bar .icon { background: var(--paper); }

  .card--brand .card__inner {
    display: flex; align-items: center; justify-content: center;
  }
</style>
</head>
<body>

  <section class="card card--contact" aria-label="Contact side">
    <div class="card__inner">
      <div class="brand">
        <span class="brand__dot"></span>
        <span class="brand__name">KLV Photography</span>
      </div>

      <div class="person">
        <p class="person__name">Gareth Pindle</p>
        <p class="person__role">General Manager</p>
      </div>

      <div class="contact-band"></div>

      <ul class="contact-list">
        <li>
          <span class="icon"><svg viewBox="0 0 16 16"><path d="M4 1h3l1 4-2 1a8 8 0 0 0 4 4l1-2 4 1v3c0 1-1 2-2 2A13 13 0 0 1 2 3c0-1 1-2 2-2z" fill="#fff"/></svg></span>
          <span>0455 917 263</span>
        </li>
        <li>
          <span class="icon"><svg viewBox="0 0 16 16"><rect x="4" y="1" width="8" height="14" rx="1.5" fill="none" stroke="#fff" stroke-width="1.6"/><circle cx="8" cy="12.5" r="1" fill="#fff"/></svg></span>
          <span>08 9412 5530</span>
        </li>
        <li>
          <span class="icon"><svg viewBox="0 0 16 16"><rect x="1.5" y="3.5" width="13" height="9" fill="none" stroke="#fff" stroke-width="1.6"/><path d="M1.5 3.5 8 9l6.5-5.5" fill="none" stroke="#fff" stroke-width="1.6"/></svg></span>
          <span>gareth@klvphotography-example.com.au</span>
        </li>
        <li>
          <span class="icon"><svg viewBox="0 0 16 16"><circle cx="8" cy="8" r="6.3" fill="none" stroke="#fff" stroke-width="1.5"/><path d="M1.7 8h12.6M8 1.7c-3 3.5-3 9 0 12.6M8 1.7c3 3.5 3 9 0 12.6" fill="none" stroke="#fff" stroke-width="1.2"/></svg></span>
          <span>www.klvphotography-example.com.au</span>
        </li>
      </ul>

      <div class="address-bar">
        <span class="icon"><svg viewBox="0 0 16 16"><path d="M8 1a5 5 0 0 0-5 5c0 4 5 9 5 9s5-5 5-9a5 5 0 0 0-5-5z" fill="#26272a"/><circle cx="8" cy="6" r="1.8" fill="#fff"/></svg></span>
        <span>14 Harbour Lane, Level 3, Perth WA</span>
      </div>
    </div>
  </section>

  <section class="card card--brand" aria-label="Logo side">
    <div class="card__inner">
      <div class="brand">
        <span class="brand__dot"></span>
        <span class="brand__name">KLV Photography</span>
      </div>
    </div>
  </section>

</body>
</html>
```